Glasses Promo

I am an optometrist, and we want to get our contact lens buying patients into the habit if buying glasses, too. It's not healthy to be stranded in contact lenses, with no viable glasses options. This post-card sized card would be handed out to all patients that are purchasing contact lenses from the practice, offering a complete pair of glasses, including frames, Vorne lenses, and a one year warranty, starting at $59.
Suggestion for text: buy a year supply of contact lenses and get a complete pair of glasses (new frame, vorne lenses, 1 year warranty) for $59
Updates

Project is now guaranteed / committed.  :) Let's see what you've got!

Target Market(s)

18-40 mixed male / female, quality, 'affordable luxury'

Industry/Entity Type

Promo

Requirements
Must have
• our logo (either one), vorne logo. simple, clean, premium feel.
limit one pair per patient. it should have our address and website. (ideas/info at our website: pennrockoptic.com )
simple, clean, would like a visual reference to glasses, either outline, silhouette, abstract, whatnot. be creative! :)
Nice to have
• frendlio quillo and m+ logos
Should not have
• dinosaurs. although they are awesome.

```html
<!DOCTYPE html>
<html lang="en">
<head>
<meta charset="utf-8">
<title>Glasses Promo Postcard</title>
<link href="https://fonts.googleapis.com/css2?family=Roboto+Condensed:wght@400&family=Mulish:wght@400;600;700&family=Arimo:wght@400;700&display=swap" rel="stylesheet">
<style>
  :root {
    --bg: #e9e6e1;
    --card: #ffffff;
    --purple: #6b2570;
    --purple-text: #6d2c73;
    --grey-text: #6e6e6e;
    --dark: #333333;
    --line: #8a8a8a;
    --vorne-blue: #1f4fa3;
    --photo-a: #c9b28a;
    --photo-b: #6e5a48;
  }
  * { margin: 0; padding: 0; box-sizing: border-box; }
  html, body { width: 1200px; height: 491px; overflow: hidden; background: var(--bg); }
  .canvas { position: relative; width: 1200px; height: 491px; }

  .card { position: absolute; background: var(--card); box-shadow: 0 2px 6px rgba(0,0,0,.25); overflow: hidden; }
  .card--front { left: 29px; top: 26px; width: 564px; height: 435px; }
  .card--back { left: 612px; top: 30px; width: 564px; height: 432px; }

  .brand { position: absolute; display: flex; align-items: center; gap: 8px; }
  .brand__mark { width: 54px; height: 54px; border: 3px solid var(--purple); border-radius: 4px; }
  .brand__name { font-family: "Mulish", sans-serif; font-weight: 700; color: var(--purple-text); font-size: 19px; letter-spacing: .5px; line-height: 1; }
  .brand__sub { font-family: "Mulish", sans-serif; font-weight: 700; color: var(--grey-text); font-size: 14px; letter-spacing: .5px; margin-top: 5px; }
  .card--front .brand { left: 26px; top: 24px; }

  .offer-band { position: absolute; left: 1px; top: 92px; width: 368px; height: 252px; background: var(--purple); }
  .offer-band__headline { position: absolute; left: 27px; top: 56px; font-family: "Roboto Condensed", sans-serif; color: #fff; font-size: 30px; line-height: 33px; }
  .social { position: absolute; left: 95px; top: 210px; display: flex; align-items: center; gap: 8px; font-family: "Arimo", sans-serif; font-size: 11px; color: #fff; }
  .social__label { font-size: 12px; margin-right: 4px; }
  .social__item { display: flex; align-items: center; gap: 3px; }
  .social__dot { width: 9px; height: 9px; background: #fff; opacity: .85; }

  .portrait { position: absolute; left: 354px; top: 76px; width: 210px; height: 252px; border: 1px solid #4a3f8f; background: linear-gradient(160deg, var(--photo-a), var(--photo-b)); }

  .price-line { position: absolute; left: 38px; top: 360px; font-family: "Mulish", sans-serif; font-size: 19px; color: var(--grey-text); line-height: 28px; }
  .price-line__only { color: var(--purple-text); font-weight: 700; font-size: 21px; }
  .price-line__amount { color: var(--purple-text); font-weight: 700; font-size: 34px; }

  .partner { position: absolute; left: 452px; top: 373px; display: flex; align-items: center; gap: 7px; }
  .partner__square { width: 22px; height: 22px; background: var(--vorne-blue); }
  .partner__name { font-family: "Mulish", sans-serif; font-weight: 700; font-size: 24px; color: var(--vorne-blue); }

  .card--back .brand { left: 60px; top: 24px; }
  .card--back .brand__mark { width: 34px; height: 34px; border-width: 2px; border-color: #777; }
  .card--back .brand__name { font-size: 14px; color: #444; }
  .card--back .brand__sub { font-size: 10px; margin-top: 3px; }

  .decor { position: absolute; left: 20px; top: 108px; width: 260px; height: 246px; background: linear-gradient(180deg, #f2f2f2, #c9c9c9 70%, #e8e8e8); border-radius: 6px; }

  .contact { position: absolute; left: 64px; top: 368px; font-family: "Mulish", sans-serif; font-size: 14px; color: var(--dark); line-height: 18px; }
  .contact__row { display: flex; align-items: center; gap: 7px; }
  .contact__row svg { width: 11px; height: 11px; }

  .divider { position: absolute; left: 310px; top: 0; width: 1px; height: 100%; background: #bdbdbd; }
  .return-address { position: absolute; left: 323px; top: 26px; font-family: "Mulish", sans-serif; font-size: 12px; color: var(--dark); line-height: 16px; }
  .postage { position: absolute; left: 456px; top: 24px; width: 82px; height: 93px; border: 1px solid #444; font-family: "Arimo", sans-serif; font-size: 9.5px; text-align: center; line-height: 12px; padding-top: 5px; color: #111; }
  .postage b { font-weight: 700; }
  .recipient { position: absolute; left: 330px; top: 164px; width: 214px; font-family: "Mulish", sans-serif; font-size: 14px; color: var(--dark); }
  .recipient__line { border-bottom: 1px solid var(--line); height: 42px; }
  .recipient__line:first-of-type { height: 36px; }
</style>
</head>
<body>
<div class="canvas">

  <section class="card card--front">
    <div class="brand">
      <div class="brand__mark"></div>
      <div>
        <div class="brand__name">PENNROCK OPTIC</div>
        <div class="brand__sub">ASSOCIATES</div>
      </div>
    </div>

    <div class="offer-band">
      <p class="offer-band__headline">Buy a Year Supply of<br>Contact Lenses<br>and Get &nbsp;a Complete<br>Pair of Glasses</p>
      <div class="social">
        <span class="social__label">Follow Us</span>
        <span class="social__item"><span class="social__dot"></span>quillo</span>
        <span class="social__item"><span class="social__dot"></span>frendlio</span>
        <span class="social__item"><span class="social__dot"></span>m+</span>
      </div>
    </div>

    <div class="portrait" role="img" aria-label="Photo of a young woman wearing black-framed glasses"></div>

    <p class="price-line">New Frame, Vorne Lenses,<br>1 Year Warranty &nbsp;all this for <span class="price-line__only">Only</span> <span class="price-line__amount">$59</span></p>

    <div class="partner">
      <span class="partner__square"></span>
      <span class="partner__name">Vorne</span>
    </div>
  </section>

  <section class="card card--back">
    <div class="brand">
      <div class="brand__mark"></div>
      <div>
        <div class="brand__name">PENNROCK OPTIC</div>
        <div class="brand__sub">ASSOCIATES</div>
      </div>
    </div>

    <div class="decor" role="img" aria-label="Silver illustration of a pair of eyeglasses"></div>

    <div class="contact">
      <div class="contact__row">
        <svg viewBox="0 0 12 12"><path d="M2 1h3l1 3-2 1a7 7 0 0 0 3 3l1-2 3 1v3c-6 0-9-3-9-9z" fill="none" stroke="#333" stroke-width="1.2"/></svg>
        (555) 014-2020
      </div>
      <div class="contact__row">
        <svg viewBox="0 0 12 12"><rect x="1" y="3" width="10" height="7" fill="none" stroke="#333" stroke-width="1.2"/><path d="M1 3l5 4 5-4" fill="none" stroke="#333" stroke-width="1.2"/></svg>
        info@pennrockoptic.com
      </div>
      <div class="contact__row">
        <svg viewBox="0 0 12 12"><circle cx="6" cy="6" r="5" fill="none" stroke="#333" stroke-width="1.2"/><path d="M1 6h10M6 1c-3 3-3 7 0 10M6 1c3 3 3 7 0 10" fill="none" stroke="#333" stroke-width="1"/></svg>
        www.pennrockoptic.com
      </div>
    </div>

    <div class="divider"></div>

    <p class="return-address">PENNROCK OPTIC<br>820 Linden Avenue<br>Suite 4<br>Fairhaven, VA 24190</p>

    <div class="postage">Presorted<br>First Class Mail<br>US Postage<br><b>PAID</b><br>Riverton, CA<br>Permit #4417</div>

    <div class="recipient">
      <div>To,</div>
      <div class="recipient__line"></div>
      <div class="recipient__line"></div>
      <div class="recipient__line"></div>
    </div>
  </section>

</div>
</body>
</html>
```